Revolutionary Job Search/ Matching website needs Flyer Design.

We need a flyer design for our Start Up company called HireLattice.

About Us - Efficient, www.hirelattice-demo.net -is the most effective way for you to find the perfect job opportunity. We revolutionize the arduous task of sending a resume out and locating jobs that fit your skill set.
The design needs to attract our target audience (Military Active/ Vets, Students High School/ College, and The Working Class). The design should communicate
Our mission is simple- to improve the communication barriers that exists between applicants and employers.

Colors: Black, white, and a combination of the colors attached. We also want he logo incorporated into the design creatively, the color of the logo can be changed to fit design concepts.

Focus of the Flyer is to get people to go to the site and sign up for free accounts.

Design: We would like something that is young, fresh, creative but still career professional.

Target Market(s)

Working age people 16-35, Students (High School, College), Military (Vets, and Active Duty, Middle Class (20k- 100k yearly).

Industry/Entity Type

Communication

Requirements
Must have
• Creative Logo Integration, using different colors or different sizes for the logo, to fit the overall theme.

Make sure Flyer is not to wordy. More visual than words is what we want to focus on.

Should be optimized for a two sided 5.5 x 8.5 inch flyer.

```html
<!DOCTYPE html>
<html lang="en">
<head>
<meta charset="utf-8">
<title>HireLattice Flyer</title>
<link href="https://fonts.googleapis.com/css2?family=Oswald:wght@500&family=Open+Sans:wght@400;600;700&family=Roboto+Slab:wght@700&display=swap" rel="stylesheet">
<style>
  :root{
    --green:#5cb82e;
    --green-dark:#3f8f1c;
    --magenta:#d21f78;
    --orange:#f37a1f;
    --charcoal:#2f3236;
    --ink:#333;
    --white:#fff;
    --page:#eeeeee;
  }
  *{box-sizing:border-box;margin:0;padding:0}
  html,body{width:807px;height:1200px;overflow:hidden;background:var(--page)}
  body{font-family:"Open Sans",Arial,sans-serif;color:var(--ink)}
  .flyer{position:relative;width:807px;height:1200px;background:var(--white);overflow:hidden}

  .top-swoosh{position:absolute;left:0;top:0;width:807px;height:260px}
  .brand-tab{position:absolute;left:270px;top:0;width:267px;height:150px;background:var(--charcoal);border-radius:0 0 26px 26px;padding:10px}
  .brand-tab .inner{width:100%;height:100%;background:var(--white);border-radius:0 0 18px 18px;display:flex;align-items:center;justify-content:center;gap:10px}
  .brand-name{font-family:"Roboto Slab",Georgia,serif;font-weight:700;color:var(--green);font-size:34px}
  .brand-dot{width:22px;height:22px;border-radius:50%;background:var(--green)}

  .hero-photo{position:absolute;left:0;top:228px;width:807px;height:392px;background:linear-gradient(135deg,#6c7d86 0%,#b8a98c 40%,#e8c93a 62%,#5a6a70 100%)}
  .hero-curve{position:absolute;left:0;top:575px;width:807px;height:70px}

  .about{position:absolute;left:0;top:640px;width:375px;height:420px;background:var(--green);border-radius:0 40px 0 0;color:var(--white);padding:20px 22px 0 24px}
  .about-title{display:inline-block;background:var(--white);color:var(--green-dark);font-family:"Roboto Slab",Georgia,serif;font-size:32px;line-height:44px;padding:2px 30px 4px 18px;border-radius:0 24px 24px 0;margin-left:-24px}
  .point{display:flex;gap:12px;margin-top:14px;align-items:flex-start}
  .point .num{font-family:"Oswald",sans-serif;font-size:50px;line-height:48px;width:30px;flex:none}
  .point p{font-size:14px;line-height:19px;font-weight:600}
  .point p b{font-weight:700;font-size:15px}
  .signup{position:absolute;left:0;top:935px;width:355px;height:105px;background:var(--white);padding:10px 20px}
  .signup .cta{font-family:"Oswald",sans-serif;font-weight:500;font-size:24px;line-height:29px;color:var(--magenta)}
  .signup .cta span{color:var(--charcoal)}
  .signup .url{font-family:"Roboto Slab",Georgia,serif;font-size:19px;line-height:26px;color:var(--green-dark)}
  .foot-brand{position:absolute;left:0;top:1060px;width:375px;height:140px;display:flex;align-items:center;justify-content:center;gap:10px}
  .foot-brand .brand-name{font-size:28px}

  .features{position:absolute;left:375px;top:640px;width:432px;height:560px;padding:22px 24px 0}
  .features h2{font-family:"Oswald",sans-serif;font-weight:500;color:var(--magenta);font-size:36px;line-height:52px;text-align:center;letter-spacing:1px;white-space:nowrap}
  .feature-grid{display:grid;grid-template-columns:repeat(3,1fr);row-gap:10px;margin-top:10px}
  .feature{text-align:center;height:124px}
  .feature .icon{width:80px;height:80px;margin:4px auto 8px;border-radius:50%;background:var(--orange);border:4px solid var(--white);box-shadow:0 0 0 3px var(--orange);display:flex;align-items:center;justify-content:center}
  .feature .label{font-family:"Roboto Slab",Georgia,serif;font-size:13px;line-height:16px;font-weight:700;color:var(--ink)}
  .how{margin:12px auto 0;width:240px;background:var(--green);color:var(--white);font-family:"Roboto Slab",Georgia,serif;font-size:22px;line-height:32px;text-align:center;padding:3px 0 5px;border-radius:18px 0 18px 0}
  .how-text{margin:8px 10px 0;font-size:14px;line-height:19px;text-align:center}
  .social-bar{position:absolute;left:40px;top:478px;width:392px;height:82px;background:var(--charcoal);border-radius:26px 0 0 0;display:flex;align-items:center;justify-content:center;gap:18px}
  .social-bar span{width:44px;height:44px;border-radius:50%;background:#4b5056;border:2px solid var(--white)}
</style>
</head>
<body>
<div class="flyer">
  <svg class="top-swoosh" viewBox="0 0 807 260" aria-hidden="true">
    <path d="M0 150 Q400 260 807 150 L807 240 Q400 300 0 240Z" fill="var(--green)"/>
    <path d="M0 175 Q400 270 807 175" stroke="var(--white)" stroke-width="6" fill="none"/>
  </svg>
  <div class="brand-tab"><div class="inner"><span class="brand-dot"></span><span class="brand-name">HireLattice</span></div></div>

  <div class="hero-photo" role="img" aria-label="Photo of a young man in a yellow patterned shirt and glasses focused on a laptop"></div>
  <svg class="hero-curve" viewBox="0 0 807 70" preserveAspectRatio="none" aria-hidden="true">
    <path d="M0 50 Q400 -10 807 50 L807 70 L0 70Z" fill="var(--white)"/>
    <path d="M0 44 Q400 -16 807 44" stroke="var(--green)" stroke-width="6" fill="none"/>
  </svg>

  <section class="about">
    <h2 class="about-title">About Us</h2>
    <div class="point"><span class="num">1</span><p><b>www.hirelattice-demo.net</b> is the most effective way for you to find the perfect job opportunity.</p></div>
    <div class="point"><span class="num">2</span><p>We revolutionize the arduous task of sending a resume out and locating jobs that fit your skill set.</p></div>
    <div class="point"><span class="num">3</span><p>Our mission is simple - to improve the communication barriers that exists between applicants and employers.</p></div>
  </section>
  <div class="signup">
    <p class="cta">GET A GOOD JOB?<br><span>THEN SIGN UP OUR WEBSITE</span></p>
    <p class="url">www.hirelattice-demo.net</p>
  </div>
  <div class="foot-brand"><span class="brand-dot"></span><span class="brand-name">HireLattice</span></div>

  <section class="features">
    <h2>JOB MARKET FEATURES</h2>
    <div class="feature-grid">
      <div class="feature"><div class="icon"><svg width="42" height="42" viewBox="0 0 46 46" fill="none" stroke="#fff" stroke-width="3"><path d="M12 34h-2a9 9 0 0 1 1-18 12 12 0 0 1 23 2 8 8 0 0 1 0 16h-2"/><path d="M23 38V22M17 28l6-6 6 6"/></svg></div><p class="label">Upload Resume</p></div>
      <div class="feature"><div class="icon"><svg width="42" height="42" viewBox="0 0 46 46" fill="none" stroke="#fff" stroke-width="3"><rect x="8" y="6" width="22" height="30"/><circle cx="26" cy="26" r="7"/><path d="M31 31l8 8"/></svg></div><p class="label">Search Job</p></div>
      <div class="feature"><div class="icon"><svg width="42" height="42" viewBox="0 0 46 46" fill="#fff"><circle cx="16" cy="15" r="6"/><circle cx="31" cy="15" r="6"/><path d="M5 36a11 11 0 0 1 22 0zM20 36a11 11 0 0 1 22 0z"/></svg></div><p class="label">Changeable Accounts</p></div>
      <div class="feature"><div class="icon"><svg width="42" height="42" viewBox="0 0 46 46" fill="none" stroke="#fff" stroke-width="3"><rect x="6" y="8" width="20" height="26"/><rect x="20" y="14" width="20" height="26" fill="var(--orange)"/><path d="M25 22h10M25 28h10M25 34h6"/></svg></div><p class="label">Resume Translated</p></div>
      <div class="feature"><div class="icon"><svg width="42" height="42" viewBox="0 0 46 46" fill="#fff"><circle cx="19" cy="15" r="8"/><path d="M4 40a15 15 0 0 1 30 0z"/><path d="M37 16v14M30 23h14" stroke="#fff" stroke-width="3"/></svg></div><p class="label">Create an Account</p></div>
      <div class="feature"><div class="icon"><svg width="42" height="42" viewBox="0 0 46 46" fill="none" stroke="#fff" stroke-width="3"><rect x="6" y="11" width="34" height="24" rx="2"/><path d="M6 13l17 13 17-13"/></svg></div><p class="label">Post Jobs</p></div>
    </div>
    <h3 class="how">How it works?</h3>
    <p class="how-text">Lorem Ipsum is simply dummy text of the printing and typesetting industry. Lorem Ipsum has been the industry's standard dummy text ever since the 1500s.</p>
    <div class="social-bar"><span></span><span></span><span></span><span></span></div>
  </section>
</div>
</body>
</html>
```